Design some Luxury Business Cards

Design a unique luxury looking business card.
For the details to include on the card please refer to the attached document and description .
Please also remember to include our logo somewhere on the card!

Lorin Vascotte
Marketing & Concierge Manager
Alpine Butler Partners GmbH
Moosweg 23
CH-8472 Bülach / Zurich
Tel. Nr: +41 76 82 14 305
Email : info@alpinebutlerpartners.example
Website : www.alpinebutlerpartners.example

```html
<!DOCTYPE html>
<html lang="en">
<head>
<meta charset="utf-8">
<title>Alpine Butler Partners – Business Card</title>
<link rel="stylesheet" href="https://fonts.googleapis.com/css2?family=Lato:wght@400;700&display=swap">
<style>
  :root {
    --bg: #3a3b3e;
    --card: #050505;
    --text: #ffffff;
    --muted: #d9d9d9;
    --brand: #bdbdbd;
  }
  * { box-sizing: border-box; margin: 0; padding: 0; }
  html, body { width: 1200px; height: 900px; overflow: hidden; }
  body {
    background: var(--bg);
    font-family: "Lato", sans-serif;
    color: var(--text);
    position: relative;
  }
  .card {
    position: absolute;
    left: 300px;
    width: 600px;
    height: 343px;
    background: var(--card);
    border-radius: 26px;
    box-shadow: 0 10px 30px rgba(0,0,0,.35);
  }
  .card--front { top: 80px; }
  .card--back { top: 477px; }

  .brand {
    position: absolute;
    display: flex;
    align-items: center;
    gap: 12px;
  }
  .brand__dot {
    width: 14px;
    height: 14px;
    border-radius: 50%;
    background: var(--brand);
    flex: none;
  }
  .brand__name {
    font-weight: 400;
    color: var(--brand);
    white-space: nowrap;
  }
  .card--front .brand { left: 50%; top: 50%; transform: translate(-50%, -50%); }
  .card--front .brand__name { font-size: 28px; }

  .card--back .brand { right: 40px; top: 62px; }
  .card--back .brand__name { font-size: 20px; }

  .person { position: absolute; left: 40px; top: 132px; }
  .person__name { font-size: 24px; font-weight: 700; }
  .person__title { font-size: 13px; color: var(--muted); margin-top: 6px; }

  .contact {
    position: absolute; left: 40px; top: 218px;
    list-style: none; font-size: 12.5px; color: var(--muted);
  }
  .contact__item { display: flex; align-items: flex-start; gap: 12px; line-height: 1.35; margin-bottom: 5px; }
  .contact__icon { width: 14px; height: 14px; flex: none; margin-top: 1px; fill: none; stroke: var(--text); stroke-width: 1.6; }
  .contact__icon--solid { fill: var(--text); stroke: none; }
</style>
</head>
<body>
  <section class="card card--front">
    <div class="brand">
      <span class="brand__dot"></span>
      <span class="brand__name">Alpine Butler Partners</span>
    </div>
  </section>

  <section class="card card--back">
    <div class="brand">
      <span class="brand__dot"></span>
      <span class="brand__name">Alpine Butler Partners</span>
    </div>

    <div class="person">
      <h1 class="person__name">Lorin Vascotte</h1>
      <p class="person__title">Marketing &amp; Concierge Manager</p>
    </div>

    <ul class="contact">
      <li class="contact__item">
        <svg class="contact__icon" viewBox="0 0 16 16"><path d="M4 1.5l2.5 3-1.5 1.5c.8 2 2.5 3.7 4.5 4.5L11 9l3 2.5-1.5 2.5C7 14 2 9 2 3z"/></svg>
        <span>(843) 555 - 0192</span>
      </li>
      <li class="contact__item">
        <svg class="contact__icon contact__icon--solid" viewBox="0 0 16 16"><path d="M1 3h14v10H1z"/><path d="M2 4.5l6 4.5 6-4.5" fill="none" stroke="#050505" stroke-width="1.2"/></svg>
        <span>info@alpinebutlerpartners.example</span>
      </li>
      <li class="contact__item">
        <svg class="contact__icon" viewBox="0 0 16 16"><path d="M6.5 9.5l3-3M5 8l-2 2a2.5 2.5 0 003.5 3.5l2-2M11 8l2-2a2.5 2.5 0 00-3.5-3.5l-2 2"/></svg>
        <span>www.alpinebutlerpartners.example</span>
      </li>
      <li class="contact__item">
        <svg class="contact__icon contact__icon--solid" viewBox="0 0 16 16"><path d="M8 1a5 5 0 015 5c0 4-5 9-5 9S3 10 3 6a5 5 0 015-5zm0 3a2 2 0 100 4 2 2 0 000-4z" fill-rule="evenodd"/></svg>
        <span>Alpine Butler Partners GmbH Moosweg 23<br>CH-8472 Bülach / Zurich</span>
      </li>
    </ul>
  </section>
</body>
</html>
```